Need webdesign for service company that provides Car hiring service and transit service

We need a web design for a company that provides airport transit services and transport services including Limo, Corporate cars, Disability transit, Family transit service. We need is a simple and professional design.

Below is site which we like and also offer the same service http://www.ridelyntrek.com.au/

Reason: Waiting for the Feedback from multiple stakeholders. Need the time to select and approve the design

Target Market(s)

Tourism, Travel

Industry/Entity Type

Airport

Number of Pages Required

3 page

Font styles to use
Decorative
Script

Requirements
Must have
• Simple and Professional, Site we like http://www.ridelyntrek.com.au/ and also need to mobile friendly
Should not have
• Shouldn't have too many images

```html
<!DOCTYPE html>
<html lang="en">
<head>
<meta charset="utf-8">
<title>Ridewell – Private &amp; Business Transport</title>
<link rel="stylesheet" href="https://fonts.googleapis.com/css2?family=Lato:wght@400;700&family=Crimson+Text:wght@600&display=swap">
<style>
  :root {
    --ink: #111111;
    --black: #000000;
    --white: #ffffff;
    --grey-text: #6b6b6b;
    --band-top: #e6e6e6;
    --button: #767274;
    --field-icon-bg: #f4f4f4;
    --services-bg: rgba(20, 18, 18, 0.82);
    --divider: rgba(255, 255, 255, 0.35);
  }
  * { box-sizing: border-box; margin: 0; padding: 0; }
  html, body { width: 1200px; height: 907px; overflow: hidden; background: var(--white); }
  body { font-family: "Lato", sans-serif; color: var(--ink); }
  .page { position: relative; width: 1200px; height: 907px; overflow: hidden; }

  .top-rule { position: absolute; left: 0; top: 0; width: 1200px; height: 5px; background: var(--black); }

  /* Header */
  .site-header { position: absolute; left: 0; top: 5px; width: 1200px; height: 124px; background: var(--white); }
  .brand-name { position: absolute; left: 101px; top: 38px; font-size: 41px; font-weight: 400;
    letter-spacing: -0.5px; line-height: 1; color: var(--ink); }

  .header-tools { position: absolute; top: 34px; left: 777px; display: flex; align-items: center; }
  .diamond-btn { width: 51px; height: 51px; display: block; }
  .phone-number { font-size: 19px; font-weight: 700; margin: 0 33px 0 12px; letter-spacing: 0.2px; }
  .header-tools .diamond-btn + .diamond-btn { margin-left: 8px; }

  /* Intro band */
  .intro { position: absolute; left: 0; top: 129px; width: 1200px; height: 138px;
    background: linear-gradient(180deg, var(--band-top) 0%, var(--white) 100%); text-align: center; }
  .intro-title { position: absolute; left: 419px; width: 362px; top: 32px; height: 40px;
    font-family: "Crimson Text", serif; font-weight: 600; font-size: 36px; line-height: 40px; }
  .intro-title .amp { font-size: 44px; }
  .intro-rule { position: absolute; top: 72px; height: 1px; background: var(--ink); }
  .intro-rule.left { left: 419px; width: 155px; }
  .intro-rule.right { left: 627px; width: 154px; }
  .intro-sub { position: absolute; left: 0; width: 1200px; top: 73px; font-size: 21px; color: var(--grey-text); letter-spacing: 0.3px; }

  /* Hero */
  .hero-photo { position: absolute; left: 0; top: 267px; width: 1200px; height: 594px;
    background:
      radial-gradient(ellipse 55% 45% at 85% 58%, rgba(232, 140, 80, 0.85), rgba(232,140,80,0) 70%),
      radial-gradient(ellipse 35% 40% at 33% 62%, rgba(180, 180, 185, 0.55), rgba(180,180,185,0) 70%),
      linear-gradient(180deg, #5a4d48 0%, #7a6258 40%, #5c4238 62%, #2c2626 100%); }

  .quote-box { position: absolute; left: 751px; top: 366px; width: 351px; height: 326px; background: var(--black); }
  .quote-title { position: absolute; top: 20px; width: 100%; text-align: center; color: var(--white);
    font-size: 25px; font-weight: 700; letter-spacing: 0.2px; }
  .field { position: absolute; left: 20px; width: 311px; background: var(--white); display: flex; }
  .field-icon { width: 33px; border-right: 1px solid #dddddd; background: var(--field-icon-bg);
    display: flex; align-items: center; justify-content: center; }
  .field-text { padding-left: 12px; font-size: 12.5px; display: flex; flex-direction: column; justify-content: center; }
  .field.origin { top: 71px; height: 38px; }
  .field.destination { top: 123px; height: 37px; }
  .field.options { top: 175px; height: 60px; }
  .option-line + .option-line { margin-top: 10px; display: flex; align-items: center; }
  .plus-box { width: 16px; height: 16px; border: 1px solid #999; margin-right: 9px; display: inline-flex; align-items: center; justify-content: center; }
  .estimate-btn { position: absolute; left: 20px; top: 258px; width: 311px; height: 42px; background: var(--button);
    color: var(--white); font-size: 20px; font-weight: 700; text-align: center; line-height: 42px; letter-spacing: 0.3px; border: 0; font-family: inherit; }

  /* Services */
  .services { position: absolute; left: 0; top: 749px; width: 1200px; height: 112px; background: var(--services-bg); }
  .service { position: absolute; top: 16px; text-align: center; color: var(--white); }
  .service svg { display: block; margin: 0 auto; height: 42px; }
  .service-label { font-size: 17px; font-weight: 700; margin-top: 12px; white-space: nowrap; }
  .svc-corporate { left: 100px; width: 152px; }
  .svc-limo { left: 362px; width: 138px; }
  .svc-disability { left: 612px; width: 172px; }
  .svc-family { left: 891px; width: 210px; }
  .divider { position: absolute; top: 18px; width: 1px; height: 66px; background: var(--divider); }

  /* Footer */
  .site-footer { position: absolute; left: 0; top: 861px; width: 1200px; height: 46px; background: var(--black); }
  .copyright { position: absolute; left: 100px; top: 14px; color: var(--white); font-size: 14px; }
  .social { position: absolute; left: 1004px; top: 8px; display: flex; gap: 6px; }
  .social svg { width: 30px; height: 30px; }
</style>
</head>
<body>
<div class="page">
  <div class="top-rule"></div>

  <header class="site-header">
    <div class="brand-name">RIDEWELL</div>

    <div class="header-tools">
      <svg class="diamond-btn" viewBox="0 0 51 51" aria-label="Call">
        <rect x="10" y="10" width="31" height="31" transform="rotate(45 25.5 25.5)" fill="none" stroke="#111" stroke-width="1.5"/>
        <path d="M19 17c1-1 2.5-1 3 0l2 3c.5 1 0 2-.8 2.5l-1 .6c.8 2 2.5 3.8 4.5 4.7l.6-1c.6-.8 1.6-1.2 2.5-.7l3 2c1 .6 1 2 0 3l-1.5 1.3c-1.5 1.2-5 .5-8.5-3s-4.7-7-3.4-8.6z" fill="#111"/>
      </svg>
      <span class="phone-number">123 456 7890</span>
      <svg class="diamond-btn" viewBox="0 0 51 51" aria-label="Menu">
        <rect x="10" y="10" width="31" height="31" transform="rotate(45 25.5 25.5)" fill="none" stroke="#111" stroke-width="1.5"/>
        <rect x="16" y="18" width="19" height="3" rx="1.5" fill="#111"/>
        <rect x="16" y="24" width="19" height="3" rx="1.5" fill="#111"/>
        <rect x="16" y="30" width="19" height="3" rx="1.5" fill="#111"/>
      </svg>
      <svg class="diamond-btn" viewBox="0 0 51 51" aria-label="Search">
        <rect x="10" y="10" width="31" height="31" transform="rotate(45 25.5 25.5)" fill="none" stroke="#111" stroke-width="1.5"/>
        <circle cx="24" cy="24" r="6.5" fill="none" stroke="#111" stroke-width="2.4"/>
        <line x1="28.7" y1="28.7" x2="33" y2="33" stroke="#111" stroke-width="2.6" stroke-linecap="round"/>
      </svg>
    </div>
  </header>

  <section class="intro">
    <h1 class="intro-title">Private <span class="amp">&amp;</span> Business</h1>
    <div class="intro-rule left"></div>
    <div class="intro-rule right"></div>
    <p class="intro-sub">Personalised Transport Services</p>
  </section>

  <div class="hero-photo" role="img" aria-label="Silver sports car driving on an open road at sunset"></div>

  <form class="quote-box">
    <h2 class="quote-title">GET INSTANT QUOTE</h2>
    <div class="field origin">
      <div class="field-icon"><svg width="12" height="12" viewBox="0 0 12 12"><circle cx="6" cy="6" r="5" fill="none" stroke="#111" stroke-width="1.2"/></svg></div>
      <div class="field-text">Origin ( Public Location Or Exact Address )</div>
    </div>
    <div class="field destination">
      <div class="field-icon"><svg width="10" height="15" viewBox="0 0 10 15"><path d="M5 0a5 5 0 0 1 5 5c0 3.5-5 10-5 10S0 8.5 0 5a5 5 0 0 1 5-5z" fill="#222"/><circle cx="5" cy="5" r="1.8" fill="#fff"/></svg></div>
      <div class="field-text">Destination ( Public Location Or Exact Address )</div>
    </div>
    <div class="field options">
      <div class="field-icon"><svg width="12" height="12" viewBox="0 0 12 12"><circle cx="6" cy="6" r="5" fill="none" stroke="#111" stroke-width="1.2"/></svg></div>
      <div class="field-text">
        <div class="option-line">Show other vehicles</div>
        <div class="option-line"><span class="plus-box"><svg width="8" height="8" viewBox="0 0 8 8"><path d="M4 0v8M0 4h8" stroke="#111" stroke-width="1.6"/></svg></span>Add Stops</div>
      </div>
    </div>
    <button type="button" class="estimate-btn">ESTIMATE FARE</button>
  </form>

  <section class="services">
    <div class="service svc-corporate">
      <svg viewBox="0 0 60 42" aria-hidden="true">
        <path d="M4 30v-7c0-2 1.5-3 3.5-3.5L16 18l6-6c1.5-1.3 3-2 5-2h10c2 0 3.5.7 5 2l5 6 7 1.5c2 .5 3 1.5 3 3.5V30z" fill="#fff"/>
        <path d="M21 18l4-5h6v5zM34 18v-5h4l4 5z" fill="#333"/>
        <circle cx="16" cy="30" r="5" fill="#fff" stroke="#333" stroke-width="2.5"/>
        <circle cx="44" cy="30" r="5" fill="#fff" stroke="#333" stroke-width="2.5"/>
      </svg>
      <div class="service-label">CORPORATE CARS</div>
    </div>
    <div class="divider" style="left:304px"></div>
    <div class="service svc-limo">
      <svg viewBox="0 0 50 42" aria-hidden="true">
        <path d="M8 14l3-8c.5-1.3 1.5-2 3-2h22c1.5 0 2.5.7 3 2l3 8h2c1 0 2 1 2 2v14c0 1-1 2-2 2H4c-1 0-2-1-2-2V16c0-1 1-2 2-2z" fill="#fff"/>
        <path d="M12 14l2.5-6h21l2.5 6z" fill="#333"/>
        <rect x="17" y="18" width="16" height="9" fill="#333"/>
        <path d="M19 19v7M22 19v7M25 19v7M28 19v7M31 19v7" stroke="#fff" stroke-width="1"/>
        <circle cx="9" cy="22" r="2.5" fill="#333"/><circle cx="41" cy="22" r="2.5" fill="#333"/>
        <rect x="5" y="32" width="6" height="5" fill="#fff"/><rect x="39" y="32" width="6" height="5" fill="#fff"/>
      </svg>
      <div class="service-label">LIMO SERVICE</div>
    </div>
    <div class="divider" style="left:560px"></div>
    <div class="service svc-disability">
      <svg viewBox="0 0 48 42" aria-hidden="true">
        <circle cx="18" cy="4" r="4" fill="#fff"/>
        <path d="M16 10h4v9h10l5 12 4-1.5 1 3-7 2.5-5-12H16z" fill="#fff"/>
        <path d="M12 17a12 12 0 1 0 18 16" fill="none" stroke="#fff" stroke-width="3.5"/>
      </svg>
      <div class="service-label">DISABILITY TRANSIT</div>
    </div>
    <div class="divider" style="left:834px"></div>
    <div class="service svc-family">
      <svg viewBox="0 0 60 42" aria-hidden="true">
        <path d="M5 6c0-4 4-6 14-6s14 2 14 6v28c0 1.5-1 2-2 2H7c-1 0-2-.5-2-2z" fill="#fff"/>
        <rect x="8" y="7" width="22" height="13" fill="#333"/>
        <rect x="12" y="2" width="14" height="2.5" fill="#333"/>
        <circle cx="10" cy="28" r="2" fill="#333"/><circle cx="28" cy="28" r="2" fill="#333"/>
        <rect x="7" y="36" width="5" height="5" fill="#fff"/><rect x="26" y="36" width="5" height="5" fill="#fff"/>
        <circle cx="42" cy="20" r="2.3" fill="#fff"/><path d="M39.5 24h5v7h-1.5v8h-2v-8h-1.5z" fill="#fff"/>
        <circle cx="52" cy="20" r="2.3" fill="#fff"/><path d="M49.5 24h5l1.5 8h-2v7h-4v-7h-2z" fill="#fff"/>
        <circle cx="47" cy="27" r="1.6" fill="#fff"/><path d="M45.5 30h3v9h-3z" fill="#fff"/>
      </svg>
      <div class="service-label">FAMILY TRANSIT SERVICE</div>
    </div>
  </section>

  <footer class="site-footer">
    <p class="copyright">Copyright © 2017 RIDEWELL. All Rights Reserved.</p>
    <div class="social">
      <svg viewBox="0 0 30 30" aria-label="Social link"><rect x="6" y="6" width="18" height="18" transform="rotate(45 15 15)" fill="none" stroke="#fff" stroke-width="1.2"/></svg>
      <svg viewBox="0 0 30 30" aria-label="Social link"><rect x="6" y="6" width="18" height="18" transform="rotate(45 15 15)" fill="none" stroke="#fff" stroke-width="1.2"/></svg>
      <svg viewBox="0 0 30 30" aria-label="Social link"><rect x="6" y="6" width="18" height="18" transform="rotate(45 15 15)" fill="none" stroke="#fff" stroke-width="1.2"/></svg>
    </div>
  </footer>
</div>
</body>
</html>
```